Dental clinic brochure design (Z fold)

We need a new brochure design made for our dental clinic - Brackenfold Dental Surgery. One side is in English, the other is in Vietnamese - all text and translations provided in brochure sample with further instructions in word doc. We require a brochure design in a Z fold to convey a family friendly dental clinic, incorporating our logo colour into the theme and designers choice on complimentary colours. Additional high quality images are provided for use if required or free to use own images.

Colors
33b8a4
00a990
86cfc6

Requirements
Must have
• Easy to read font, flows from text to pictures and page to page
• At least 2 dental images

```html
<!DOCTYPE html>
<html lang="en">
<head>
<meta charset="utf-8">
<title>Brackenfold Dental Surgery – Brochure Inside Spread</title>
<link href="https://fonts.googleapis.com/css2?family=Catamaran:wght@800&family=PT+Sans&family=PT+Sans+Narrow&display=swap" rel="stylesheet">
<style>
  :root{
    --teal:#1bbbaa;
    --teal-deep:#00a990;
    --teal-soft:#86cfc6;
    --white:#ffffff;
    --ink:#111111;
    --rule:#1a1a1a;
  }
  *{margin:0;padding:0;box-sizing:border-box}
  html,body{width:1200px;height:916px;overflow:hidden;background:var(--white)}
  body{position:relative;font-family:"PT Sans",sans-serif;color:var(--ink)}

  .page-label{position:absolute;top:72px;width:342px;text-align:center;font-size:14px;letter-spacing:.3px}

  .panel{position:absolute;top:100px;width:342px;height:716px;background:var(--teal)}
  .panel--benefits{left:85px;border-right:1px solid var(--rule)}
  .panel--promos{left:427px}
  .panel--team{left:769px;border:1px solid var(--rule)}

  .panel-title{position:absolute;top:34px;left:0;width:100%;text-align:center;
    font-family:"Catamaran",sans-serif;font-weight:800;font-size:29px;line-height:29px;
    color:var(--white);letter-spacing:.8px;text-transform:uppercase}
  .title-divider{position:absolute;top:100px;left:97px;width:148px;height:12px}

  .card{position:absolute;left:28px;width:287px;background:var(--white);border-radius:12px;
    display:flex;align-items:center;justify-content:center;text-align:center;
    font-size:19px;line-height:21.8px;padding:0 8px}
  .card::after{content:"";position:absolute;left:20px;right:20px;bottom:-9px;height:9px;
    background:radial-gradient(ellipse at top,rgba(0,70,60,.45),rgba(0,70,60,0) 70%)}

  .photo-kids{position:absolute;left:0;bottom:0;width:342px;height:185px;
    background:linear-gradient(90deg,#c9d84a 0%,#e79ab8 35%,#3a4a9a 55%,#f0d23c 75%,#9fd3ef 100%)}

  .fine-print{position:absolute;left:0;top:668px;width:100%;text-align:center;color:var(--white);font-size:12.5px;line-height:14.5px}
  .fine-print .rule-row{display:flex;align-items:center;gap:6px}
  .fine-print .rule-row::before,.fine-print .rule-row::after{content:"";flex:1;height:1px;background:var(--white)}

  .dentist-list{position:absolute;left:31px;top:154px;width:280px;height:217px;background:var(--white);border-radius:10px;
    list-style:none;font-family:"PT Sans Narrow",sans-serif;font-size:15px;padding:6px 14px}
  .dentist-list li{height:35.2px;display:flex;align-items:center;justify-content:center;white-space:nowrap;
    border-bottom:2px solid var(--teal)}
  .dentist-list li:last-child{border-bottom:none}
  .dentist-list::after{content:"";position:absolute;left:20px;right:20px;bottom:-9px;height:9px;
    background:radial-gradient(ellipse at top,rgba(0,70,60,.45),rgba(0,70,60,0) 70%)}

  .map-card{position:absolute;left:31px;top:399px;width:280px;height:216px;background:var(--white);border-radius:10px}
  .map-card::after{content:"";position:absolute;left:20px;right:20px;bottom:-9px;height:9px;
    background:radial-gradient(ellipse at top,rgba(0,70,60,.45),rgba(0,70,60,0) 70%)}
  .map-area{position:absolute;left:42px;top:4px;width:180px;height:208px;
    background:linear-gradient(160deg,#f2f2f2,#dcdcdc)}
  .map-label{position:absolute;right:10px;top:10px;font-size:12px;display:flex;align-items:center;gap:4px}

  .contact{position:absolute;left:0;top:634px;width:100%;text-align:center;color:var(--white)}
  .contact-heading{display:flex;align-items:center;justify-content:center;gap:8px;font-size:15px;margin-bottom:2px}
  .contact-heading::before,.contact-heading::after{content:"";width:52px;height:1px;background:var(--teal-soft)}
  .contact p{font-size:12.2px;line-height:14.6px}
</style>
</head>
<body>

  <div class="page-label" style="left:85px">Page 04</div>
  <div class="page-label" style="left:427px">Page 05</div>
  <div class="page-label" style="left:769px">Page 06</div>

  <!-- Page 04 -->
  <section class="panel panel--benefits">
    <h2 class="panel-title">Child Dental<br>Benefits Scheme</h2>
    <svg class="title-divider" viewBox="0 0 148 12"><path d="M0 1H64L74 10L84 1H148" fill="none" stroke="#fff" stroke-width="2"/></svg>
    <div class="card" style="top:149px;height:111px">A dental benefits program is available for eligible children aged 2 to 17 and will receive $1000 for dental treatments.</div>
    <div class="card" style="top:310px;height:110px">To check if your<br>children are eligible<br>call us on 9400 2815</div>
    <div class="photo-kids" role="img" aria-label="Photo of five smiling children standing together"></div>
  </section>

  <!-- Page 05 -->
  <section class="panel panel--promos">
    <h2 class="panel-title">Special<br>Promotions</h2>
    <svg class="title-divider" viewBox="0 0 148 12"><path d="M0 1H64L74 10L84 1H148" fill="none" stroke="#fff" stroke-width="2"/></svg>
    <div class="card" style="top:149px;height:111px">Gap free dental check-up, clean &amp; x-rays for all health insurances</div>
    <div class="card" style="top:297px;height:111px">At home whitening kit now $199<br>limited time only<br>(normally $395)</div>
    <div class="card" style="top:464px;height:110px">Braces, dentures and implants<br>are available at our clinic</div>
    <div class="fine-print">
      <div class="rule-row">Conditions apply</div>
      <div>Ask staff for more information</div>
    </div>
  </section>

  <!-- Page 06 -->
  <section class="panel panel--team">
    <h2 class="panel-title">All of the<br>Dentists' Names</h2>
    <svg class="title-divider" viewBox="0 0 148 12"><path d="M0 1H64L74 10L84 1H148" fill="none" stroke="#fff" stroke-width="2"/></svg>
    <ul class="dentist-list">
      <li>Dr Mai Tran&nbsp; BDSc (Melb), ICCDE</li>
      <li>Dr Quang Vo&nbsp; BDSc (Melb), FICCDE</li>
      <li>FRACDS, PGradDipCD Implants (Melb)</li>
      <li>Dr Thu Nguyen&nbsp; BHscMdent (Latrobe)</li>
      <li>Dr Daniel Ly&nbsp; BHsc Mdent (Latrobe), FRACDS</li>
      <li>Dr Anna Ly&nbsp; BDS (Adl)</li>
    </ul>
    <div class="map-card">
      <div class="map-area" role="img" aria-label="Street map showing the clinic location near the library, shops and train station"></div>
      <div class="map-label"><svg width="7" height="12" viewBox="0 0 7 12"><path d="M7 0V12L0 6Z" fill="#999"/></svg>Map</div>
    </div>
    <div class="contact">
      <div class="contact-heading">Address</div>
      <p>48 Brackenfold Road, Westvale, VIC 3099</p>
      <p>Phone: (03) 9400 2815</p>
      <p>Email: admin@brackenfolddental.com.au</p>
    </div>
  </section>

</body>
</html>
```